Migration Lawyers

Company: Dunstan & Co Lawyers & Migration Agents

Name: Graham Dunstan BEc, LLB
Address: Level 18, 72 Hollis Street
Sydney, NSW, Australia 2000

Ph: +61 2 9384 5207
M: 0428316540
E: graham@permitpath-example.org.au
W: www.permitpath-example.org.au

Target Market(s)

Migration Clients

Industry/Entity Type

It Company

Font styles to use
Script

Requirements
Must have
• Logo
Should not have
• Please scale the format to the printing size attached

```html
<!DOCTYPE html>
<html lang="en">
<head>
<meta charset="utf-8">
<title>Dunstan &amp; Co — Business Card</title>
<link rel="stylesheet" href="https://fonts.googleapis.com/css2?family=Tinos:wght@700&family=Didact+Gothic&family=Kalam:wght@400&display=swap">
<style>
  :root {
    --page-bg: #e4e2df;
    --card-black: #050203;
    --card-red: #c3262d;
    --card-red-deep: #6d0f14;
    --card-white: #ffffff;
    --card-grey: #f1f1f1;
    --ink: #111111;
    --ink-soft: #2a2a2a;
    --ring: #c9c9c9;
  }
  * { box-sizing: border-box; margin: 0; padding: 0; }
  html, body {
    width: 1200px;
    height: 871px;
    overflow: hidden;
    background: var(--page-bg);
  }
  .canvas {
    width: 1200px;
    height: 871px;
    display: flex;
    align-items: center;
    justify-content: center;
    gap: 40px;
  }
  .card {
    position: relative;
    width: 540px;
    height: 330px;
    overflow: hidden;
    box-shadow: 0 6px 18px rgba(0,0,0,0.25);
  }

  /* Front side */
  .card--front {
    background:
      radial-gradient(ellipse 46% 62% at 50% 40%, var(--card-red) 0%, var(--card-red-deep) 55%, var(--card-black) 100%);
  }
  .brand {
    position: absolute;
    left: 150px;
    top: 108px;
    display: flex;
    align-items: center;
    gap: 14px;
  }
  .brand__circle {
    width: 62px;
    height: 62px;
    border: 2px solid var(--ink);
    border-radius: 50%;
    flex: none;
  }
  .brand__text {
    font-family: "Tinos", "Times New Roman", serif;
    font-weight: 700;
    color: var(--ink);
    line-height: 1.05;
  }
  .brand__name { font-size: 34px; display: block; }
  .brand__tagline { font-size: 14px; display: block; }

  /* Back side */
  .card--back {
    background: linear-gradient(200deg, var(--card-grey) 0%, var(--card-white) 45%);
  }
  .holder {
    position: absolute;
    left: 38px;
    top: 34px;
    font-family: "Kalam", cursive;
    font-size: 20px;
    letter-spacing: 4px;
    color: var(--ink);
    transform: skewX(-8deg);
  }
  .address {
    position: absolute;
    left: 42px;
    top: 108px;
    font-family: "Didact Gothic", sans-serif;
    font-size: 11.5px;
    letter-spacing: 1.2px;
    line-height: 1.55;
    color: var(--ink-soft);
  }
  .contacts {
    position: absolute;
    left: 42px;
    top: 168px;
    font-family: "Didact Gothic", sans-serif;
    font-size: 11.5px;
    letter-spacing: 1.2px;
    line-height: 1.6;
    color: var(--ink-soft);
    display: grid;
    grid-template-columns: 22px auto;
  }
  .contacts dt { font-weight: 700; color: var(--ink); font-size: 9px; padding-top: 2px; }
  .decor-ring {
    position: absolute;
    right: -70px;
    bottom: -90px;
    width: 290px;
    height: 290px;
    border-radius: 50%;
    border: 3px solid var(--ring);
    opacity: 0.6;
  }
</style>
</head>
<body>
<main class="canvas">
  <section class="card card--front" aria-label="Card front">
    <div class="brand">
      <span class="brand__circle"></span>
      <span class="brand__text">
        <span class="brand__name">Dunstan &amp; Co</span>
        <span class="brand__tagline">Lawyers &amp; Migration Agents</span>
      </span>
    </div>
  </section>

  <section class="card card--back" aria-label="Card back">
    <span class="decor-ring"></span>
    <h1 class="holder">Graham Dunstan BEc, LLB</h1>
    <p class="address">Level 18, 72 Hollis Street<br>Australia, Sydney, NSW, 2000</p>
    <dl class="contacts">
      <dt>P</dt><dd>+61 2 9384 5207</dd>
      <dt>M</dt><dd>0428316540</dd>
      <dt>E</dt><dd>graham@permitpath-example.org.au</dd>
      <dt>W</dt><dd>www.permitpath-example.org.au</dd>
    </dl>
  </section>
</main>
</body>
</html>
```